Business Card Design

Quorvel Software Limited develops and sells venue and event management software called Quorvel Stagehand, which is available in the cloud or on-premise. The company was established in 1986. Most of our customers are performing arts venues, museums and festivals. Our existing design is a bit dull. We need to convey that we are both innovative and reliable.
Not all our people show their mobile phone numbers on their cards, so the design needs to work land line and mobile or land line only.

Industry/Entity Type

Software

Contact Information for Business Card

Helen Trasko
Director
Quorvel Software Limited
42B Milbrook Lane, Epsom, Surrey, KT19 4DN
Telephone: +44 (0)1372 640913
Mobile: +44 (0)7945 216804
Email: htrasko@quorvel.net
Web: www.quorvel.net

```html
<!DOCTYPE html>
<html lang="en">
<head>
<meta charset="utf-8">
<title>Quorvel Software Limited – Business Card</title>
<link rel="stylesheet" href="https://fonts.googleapis.com/css2?family=Open+Sans:wght@400;600;700&display=swap">
<style>
  :root {
    --backdrop: #eeeeef;
    --card: #ffffff;
    --navy: #0d3560;
    --blue: #0a5a9c;
    --deep: #06355f;
    --grey: #c4c6cc;
    --ink: #3a3a3a;
    --muted: #555a60;
  }
  * { box-sizing: border-box; margin: 0; padding: 0; }
  html, body { width: 1200px; height: 720px; overflow: hidden; }
  body {
    background: var(--backdrop);
    font-family: "Open Sans", Arial, sans-serif;
    position: relative;
  }
  .card {
    position: absolute;
    top: 198px;
    width: 500px;
    height: 324px;
    background: var(--card);
    box-shadow: 0 2px 10px rgba(0,0,0,0.08);
    overflow: hidden;
  }
  .card--back { left: 60px; }
  .card--front { left: 640px; }

  /* back */
  .back-band {
    position: absolute; left: 0; top: 0; bottom: 0; width: 150px;
    background: var(--blue);
  }
  .back-band-edge {
    position: absolute; left: 150px; top: 0; bottom: 0; width: 26px;
    background: var(--grey);
  }
  .back-base {
    position: absolute; left: 0; bottom: 0; width: 176px; height: 70px;
    background: var(--deep);
  }
  .back-text {
    position: absolute; left: 206px; right: 28px; top: 130px;
    color: var(--ink);
  }
  .back-tagline { font-size: 17px; font-weight: 400; }
  .back-web { margin-top: 6px; font-size: 17px; font-weight: 700; letter-spacing: 1px; }

  /* front */
  .brand {
    position: absolute; left: 42px; top: 40px;
    display: flex; align-items: center; gap: 16px;
  }
  .brand-square { width: 34px; height: 34px; background: var(--blue); }
  .brand-name {
    font-size: 46px; font-weight: 700; color: var(--navy);
    letter-spacing: 3px; line-height: 1;
  }
  .details { position: absolute; left: 42px; top: 122px; color: var(--ink); }
  .person-name { font-size: 20px; font-weight: 600; color: var(--navy); line-height: 1.1; }
  .person-title { font-size: 13px; color: var(--muted); margin-left: 4px; }
  .company { margin-top: 14px; font-size: 13px; font-weight: 700; color: var(--navy); }
  .address { font-size: 13px; }
  .contacts { margin-top: 10px; list-style: none; font-size: 13.5px; }
  .contacts li { display: flex; align-items: center; gap: 8px; line-height: 1.3; }
  .contacts svg { width: 12px; height: 12px; fill: var(--navy); flex: none; }
</style>
</head>
<body>

<section class="card card--back" aria-label="Card back">
  <div class="back-band"></div>
  <div class="back-band-edge"></div>
  <div class="back-base"></div>
  <div class="back-text">
    <p class="back-tagline">Event And Venue Management Software</p>
    <p class="back-web">www.quorvel.net</p>
  </div>
</section>

<section class="card card--front" aria-label="Card front">
  <div class="brand">
    <span class="brand-square"></span>
    <span class="brand-name">QUORVEL</span>
  </div>
  <div class="details">
    <p class="person-name">Helen Trasko</p>
    <p class="person-title">Managing Director</p>
    <p class="company">Quorvel Software Limited</p>
    <p class="address">42B Milbrook Lane, Epsom, Surrey, KT19 4DN</p>
    <ul class="contacts">
      <li><svg viewBox="0 0 12 12" aria-hidden="true"><path d="M3 0h6a1 1 0 0 1 1 1v10a1 1 0 0 1-1 1H3a1 1 0 0 1-1-1V1a1 1 0 0 1 1-1zm0 2v7h6V2z"/></svg>+44 (0)7945 216804</li>
      <li><svg viewBox="0 0 12 12" aria-hidden="true"><path d="M1 4c2-2.5 8-2.5 10 0l-1.5 1.5L8 4.5V3.8c-1.3-.4-2.7-.4-4 0v.7L2.5 5.5zM3 6h6l1 5H2z"/></svg>+44 (0)1372 640913</li>
      <li><svg viewBox="0 0 12 12" aria-hidden="true"><path d="M0 2h12v8H0zm1 1v.3l5 3.3 5-3.3V3zm0 1.5V9h10V4.5L6 7.8z"/></svg>htrasko@quorvel.net</li>
      <li><svg viewBox="0 0 12 12" aria-hidden="true"><path d="M6 0a6 6 0 1 1 0 12A6 6 0 0 1 6 0zm-4.6 5h2.2c.1-1.5.5-2.8 1.1-3.8A5 5 0 0 0 1.4 5zm3.2 0h2.8C7.3 3.4 6.7 2 6 1.3 5.3 2 4.7 3.4 4.6 5zm3.8 0h2.2a5 5 0 0 0-3.3-3.8c.6 1 1 2.3 1.1 3.8zM1.4 7a5 5 0 0 0 3.3 3.8c-.6-1-1-2.3-1.1-3.8zm3.2 0c.1 1.6.7 3 1.4 3.7.7-.7 1.3-2.1 1.4-3.7zm3.8 0c-.1 1.5-.5 2.8-1.1 3.8A5 5 0 0 0 10.6 7z"/></svg>quorvel.net</li>
    </ul>
  </div>
</section>

</body>
</html>
```